We need a banner for the top of our webpage at QuillVesta.com

We have an online tool that automatically reviews business plans. It spellchecks, rewords, re-formats and generates a new improved business plan. The banner concept should reflect this business concept. We don't want to be very formal. It should look like the business plan document is getting a treatment (similar to a spa treatment). We are changing our current website QuillVesta.com to QuillVestaPros.com. We will use your design to help us shift from our old concept to our New concept.

Banner text should say:
QuillVestaPROs.com
Our Tools, Your Way
$200 in Credits - FREE

Target Market(s)

Entrepreneurs, ambitious young people, young people 30-40 who need business help

Industry/Entity Type

Business

Font styles to use
Sans Serif

Colors

Designer to choose colors to be used in the design.

Requirements
Must have
• Must blend with the current pictures, must fit in the space allocated at the top of the page. Must bleed nicely with the information already on the right side of the top page.
Nice to have
• Make a serious topic like business help look relaxing as if the business owner is going to a Spa.
Should not have
• Should not be too, too serious. We want to lighten the front page up.

```html
<!DOCTYPE html>
<html lang="en">
<head>
<meta charset="utf-8">
<title>QuillVestaPROs.com Banner</title>
<link href="https://fonts.googleapis.com/css2?family=Montserrat:wght@500;600;700&display=swap" rel="stylesheet">
<style>
  :root {
    --backdrop: #e1e1e1;
    --navy: #2d3a57;
    --navy-light: #34425f;
    --navy-dark: #283350;
    --cyan: #12bdf0;
    --band-text: #2a3350;
    --white: #ffffff;
  }
  html, body {
    margin: 0;
    padding: 0;
    width: 1200px;
    height: 1200px;
    overflow: hidden;
    background: var(--backdrop);
  }
  .canvas {
    position: relative;
    width: 1200px;
    height: 1200px;
  }
  .banner {
    position: absolute;
    left: 78px;
    top: 445px;
    width: 1042px;
    height: 312px;
    box-shadow: 0 1px 3px rgba(0,0,0,0.25);
  }
  .banner svg { display: block; }
  .banner-text {
    font-family: 'Montserrat', sans-serif;
  }
  .site-name { fill: var(--white); font-weight: 500; font-size: 37px; }
  .tagline { fill: var(--cyan); font-weight: 700; font-size: 39px; letter-spacing: 1.5px; word-spacing: 12px; }
  .offer { fill: var(--band-text); font-weight: 600; font-size: 35px; letter-spacing: 0.5px; }
</style>
</head>
<body>
<div class="canvas">
  <div class="banner">
    <svg width="1042" height="312" viewBox="97 556 1302 390" xmlns="http://www.w3.org/2000/svg">
      <defs>
        <linearGradient id="photo-tone" x1="0" y1="0" x2="1" y2="0.3">
          <stop offset="0" stop-color="#2c3c6b"/>
          <stop offset="0.35" stop-color="#5b678a"/>
          <stop offset="0.65" stop-color="#d8d4d4"/>
          <stop offset="1" stop-color="#f2eeea"/>
        </linearGradient>
      </defs>

      <rect class="panel" x="97" y="556" width="1302" height="390" fill="var(--navy)"/>
      <g class="panel-facets">
        <polygon points="1100,556 1399,556 1399,700 1250,640" fill="var(--navy-light)"/>
        <polygon points="900,946 1150,820 1399,946" fill="var(--navy-dark)"/>
        <polygon points="1300,600 1399,560 1399,720" fill="#384765"/>
      </g>

      <polygon class="photo-area" role="img" aria-label="Photo of two businessmen in suits smiling while reviewing a tablet at a bright office table"
        points="97,556 687,556 770,660 683,946 97,946" fill="url(#photo-tone)"/>

      <polyline class="edge-accent" points="690,556 773,658 742,740" fill="none" stroke="var(--cyan)" stroke-width="5"/>

      <polygon class="offer-band" points="716,738 1399,738 1399,788 705,788" fill="var(--cyan)"/>
      <polygon class="offer-band-tail" points="705,788 727,788 722,796" fill="#0a8fbd"/>

      <g class="banner-text">
        <text class="site-name" x="810" y="664">QuillVestaPROs.com</text>
        <text class="tagline" x="810" y="717">OUR TOOLS, YOUR WAY</text>
        <text class="offer" x="810" y="776">$200 in CREDITS - FREE</text>
      </g>
    </svg>
  </div>
</div>
</body>
</html>
```